PROPERTY BROCHURE

Need an attractive layout and design for this multi-page brochure

Industry/Entity Type

Real Estate Development

Colors

Designer to choose colors to be used in the design.

```html
<!DOCTYPE html>
<html lang="en">
<head>
<meta charset="utf-8">
<title>Property Brochure – Area Profile</title>
<link href="https://fonts.googleapis.com/css2?family=Quicksand:wght@500;700&family=Lato:wght@400;700&family=Tinos&display=swap" rel="stylesheet">
<style>
  :root{
    --bg:#e9e7e4;
    --paper:#ffffff;
    --ink:#1f2530;
    --navy:#1e2633;
    --rule:#d5d8dc;
    --red:#d3121c;
    --green:#6cbf2a;
    --grey-ring:#a9adb3;
    --dark-page:#0d0d0f;
    --pie-orange:#f38e35;
    --pie-blue:#3f6fba;
    --pie-red:#c0413f;
    --pie-green:#8bb44a;
    --pie-purple:#7054a0;
    --pie-teal:#37a6c2;
  }
  *{box-sizing:border-box;margin:0;padding:0}
  html,body{width:1200px;height:900px;overflow:hidden;background:var(--bg)}
  body{position:relative;font-family:"Lato",sans-serif;color:var(--ink)}

  .page{position:absolute;width:560px;height:400px;overflow:hidden;box-shadow:0 2px 8px rgba(0,0,0,.15)}

  /* Back cover */
  .back-cover{left:320px;top:30px;background:var(--dark-page);color:#fff}
  .back-cover .interior-photo{position:absolute;inset:0;background:linear-gradient(100deg,#060607 0%,#121214 45%,#2a2c30 75%,#4a4f56 100%)}
  .back-cover .rental-stats{position:absolute;left:40px;top:100px;font-family:"Quicksand",sans-serif;font-weight:700;font-size:26px;line-height:1.2}
  .rental-stats .label{color:var(--red)}
  .rental-stats .value{color:#fff}
  .back-cover .footnote{position:absolute;left:40px;top:262px;font-size:10.5px;line-height:1.4;color:#e4e4e4}

  /* Inside spread */
  .stats-page{left:40px;top:460px;background:linear-gradient(135deg,#f7f7f8 0%,#ffffff 40%,#eef0f2 70%,#f9f9fa 100%)}
  .stats-page .pattern{position:absolute;inset:0;background:linear-gradient(160deg,rgba(220,223,227,.5),rgba(255,255,255,0) 50%,rgba(220,223,227,.45))}
  .census-table{position:absolute;left:40px;top:26px;border-collapse:collapse;font-family:"Tinos",serif;font-size:14px;background:#fff}
  .census-table td{border:1px solid #222;padding:1px 6px;height:20px}
  .census-table td:first-child{width:360px}
  .census-table td:last-child{width:90px}
  .chart-card{position:absolute;top:160px;width:230px;height:190px;background:#fff;border:1px solid var(--rule)}
  .chart-card.age{left:40px}
  .chart-card.marital{left:280px}
  .chart-card h3{font-size:9px;font-weight:400;color:#555;text-align:center;margin-top:8px}
  .chart-card svg{display:block;margin:6px auto 0}
  .legend{display:flex;flex-wrap:wrap;justify-content:center;gap:2px 8px;padding:6px 8px 0;font-size:7px;color:#555;list-style:none}
  .legend li::before{content:"";display:inline-block;width:5px;height:5px;margin-right:3px;background:var(--c)}
  .brand{font-family:"Quicksand",sans-serif;font-weight:700;color:var(--navy);font-size:20px;letter-spacing:.5px;white-space:nowrap}
  .stats-page .brand{position:absolute;left:40px;bottom:16px}

  .profile-page{left:600px;top:460px;background:var(--paper)}
  .profile-page .building-photo{position:absolute;right:0;top:40px;width:250px;height:320px;background:linear-gradient(90deg,rgba(255,255,255,1) 0%,rgba(220,224,228,.7) 25%,#b9c0c6 60%,#8d969e 100%)}
  .block{position:absolute;text-align:center}
  .block h4{font-size:7px;letter-spacing:1px;text-transform:uppercase;color:#555;font-weight:700;padding-bottom:6px;border-bottom:1px solid var(--rule)}
  .avg-age{left:20px;top:30px;width:150px}
  .avg-age .big{font-family:"Quicksand",sans-serif;font-weight:700;color:var(--green);font-size:30px;margin-top:22px}
  .dependency{left:172px;top:48px;width:140px}
  .occupation{left:20px;top:160px;width:150px;text-align:left}
  .occupation h4{text-align:center}
  .occ-row{display:flex;align-items:baseline;gap:10px;padding:6px 0 2px;border-bottom:1px solid var(--rule);position:relative}
  .occ-row .pct{font-family:"Quicksand",sans-serif;font-weight:700;font-size:18px;width:40px}
  .occ-row .pct small{font-size:7px}
  .occ-row .name{font-size:8px;color:#444}
  .occ-row::after{content:"";position:absolute;left:0;bottom:-2px;width:var(--w);height:3px;background:var(--green)}
  .ownership{left:172px;top:160px;width:140px}
  .block svg{display:block;margin:0 auto}
  .ring-label{font-size:6px;fill:#fff;font-family:"Lato",sans-serif}
  .profile-page .footer-band{position:absolute;right:0;bottom:0;width:270px;height:40px;background:linear-gradient(90deg,rgba(255,255,255,0),#d8dbde 30%,#c9cdd1)}
  .profile-page .brand{position:absolute;right:96px;bottom:12px;font-size:18px}
  .profile-page .web{position:absolute;right:14px;bottom:16px;font-size:6px;color:#444;white-space:nowrap}
</style>
</head>
<body>

<section class="page back-cover">
  <div class="interior-photo" role="img" aria-label="Dim photograph of an apartment dining and living interior"></div>
  <div class="rental-stats">
    <div class="label">Median Rental Price</div>
    <div class="value">$350 per week</div>
    <div class="label">Number of Rentals</div>
    <div class="value">446</div>
  </div>
  <p class="footnote">Based on recorded House and Unit rentals within the last 12 months (2017)<br>Based on a rolling 12 month period and may differ from calendar year statistics</p>
</section>

<section class="page stats-page">
  <div class="pattern" role="img" aria-label="Faint grey geometric background pattern"></div>
  <table class="census-table">
    <tr><td>Total population</td><td>21910</td></tr>
    <tr><td>Median household income ($/weekly)</td><td>1831</td></tr>
    <tr><td>Median age of persons</td><td>32</td></tr>
    <tr><td>Median housing loan repayment ($/monthly)</td><td>1517</td></tr>
    <tr><td>Average household size</td><td>2.8</td></tr>
  </table>

  <figure class="chart-card age">
    <h3>Age Group</h3>
    <svg width="110" height="110" viewBox="0 0 110 110">
      <g transform="rotate(-90 55 55)" fill="none" stroke-width="50">
        <circle cx="55" cy="55" r="25" pathLength="100" stroke="var(--pie-orange)" stroke-dasharray="36 100" stroke-dashoffset="0"/>
        <circle cx="55" cy="55" r="25" pathLength="100" stroke="var(--pie-blue)" stroke-dasharray="10 100" stroke-dashoffset="-36"/>
        <circle cx="55" cy="55" r="25" pathLength="100" stroke="var(--pie-red)" stroke-dasharray="13 100" stroke-dashoffset="-46"/>
        <circle cx="55" cy="55" r="25" pathLength="100" stroke="var(--pie-green)" stroke-dasharray="13 100" stroke-dashoffset="-59"/>
        <circle cx="55" cy="55" r="25" pathLength="100" stroke="var(--pie-purple)" stroke-dasharray="13 100" stroke-dashoffset="-72"/>
        <circle cx="55" cy="55" r="25" pathLength="100" stroke="var(--pie-teal)" stroke-dasharray="15 100" stroke-dashoffset="-85"/>
      </g>
    </svg>
    <ul class="legend">
      <li style="--c:var(--pie-blue)">0-14 years</li>
      <li style="--c:var(--pie-red)">15-24 years</li>
      <li style="--c:var(--pie-green)">25-34 years</li>
      <li style="--c:var(--pie-purple)">35-49 years</li>
      <li style="--c:var(--pie-teal)">50-64 years</li>
      <li style="--c:var(--pie-orange)">65+ years</li>
    </ul>
  </figure>

  <figure class="chart-card marital">
    <h3>Marital Status</h3>
    <svg width="110" height="110" viewBox="0 0 110 110">
      <g transform="rotate(-90 55 55)" fill="none" stroke-width="50">
        <circle cx="55" cy="55" r="25" pathLength="100" stroke="var(--pie-blue)" stroke-dasharray="52 100" stroke-dashoffset="0"/>
        <circle cx="55" cy="55" r="25" pathLength="100" stroke="var(--pie-red)" stroke-dasharray="43 100" stroke-dashoffset="-52"/>
        <circle cx="55" cy="55" r="25" pathLength="100" stroke="var(--pie-green)" stroke-dasharray="5 100" stroke-dashoffset="-95"/>
      </g>
    </svg>
    <ul class="legend">
      <li style="--c:var(--pie-blue)">Married</li>
      <li style="--c:var(--pie-red)">De facto</li>
      <li style="--c:var(--pie-green)">Not married</li>
    </ul>
  </figure>

  <div class="brand">Slate Ridge</div>
</section>

<section class="page profile-page">
  <div class="building-photo" role="img" aria-label="Photograph of a modern townhouse facade with balconies"></div>

  <div class="block avg-age">
    <h4>Average Age</h4>
    <div class="big">20 - 39</div>
  </div>

  <div class="block dependency">
    <h4>Dependency</h4>
    <svg width="140" height="90" viewBox="0 0 140 90">
      <g transform="rotate(-90 70 48)" fill="none" stroke-width="7">
        <circle cx="70" cy="48" r="32" pathLength="100" stroke="var(--green)" stroke-dasharray="51 100"/>
        <circle cx="70" cy="48" r="32" pathLength="100" stroke="var(--navy)" stroke-dasharray="49 100" stroke-dashoffset="-51"/>
      </g>
      <text x="70" y="46" text-anchor="middle" font-family="Quicksand, sans-serif" font-weight="700" font-size="15" fill="var(--green)">51</text>
      <text x="70" y="62" text-anchor="middle" font-family="Quicksand, sans-serif" font-weight="700" font-size="15" fill="var(--navy)">49</text>
      <rect x="8" y="34" width="38" height="10" rx="5" fill="var(--navy)"/>
      <text class="ring-label" x="27" y="41" text-anchor="middle">Dependent</text>
      <rect x="90" y="52" width="44" height="10" rx="5" fill="var(--green)"/>
      <text class="ring-label" x="112" y="59" text-anchor="middle">Independent</text>
    </svg>
  </div>

  <div class="block occupation">
    <h4>Occupation</h4>
    <div class="occ-row" style="--w:20px"><span class="pct">20<small>%</small></span><span class="name">Manufacturing</span></div>
    <div class="occ-row" style="--w:11px"><span class="pct">11<small>%</small></span><span class="name">Retail trade</span></div>
    <div class="occ-row" style="--w:11px"><span class="pct">11<small>%</small></span><span class="name">Health Care/Social</span></div>
  </div>

  <div class="block ownership">
    <h4>Ownership</h4>
    <svg width="140" height="100" viewBox="0 0 140 100">
      <g transform="rotate(-90 70 52)" fill="none" stroke-width="7">
        <circle cx="70" cy="52" r="34" pathLength="100" stroke="var(--green)" stroke-dasharray="36 100"/>
        <circle cx="70" cy="52" r="34" pathLength="100" stroke="var(--navy)" stroke-dasharray="35 100" stroke-dashoffset="-36"/>
        <circle cx="70" cy="52" r="34" pathLength="100" stroke="var(--grey-ring)" stroke-dasharray="29 100" stroke-dashoffset="-71"/>
      </g>
      <text x="70" y="42" text-anchor="middle" font-family="Quicksand, sans-serif" font-weight="700" font-size="13" fill="var(--green)">36</text>
      <text x="70" y="55" text-anchor="middle" font-family="Quicksand, sans-serif" font-weight="700" font-size="13" fill="var(--navy)">35</text>
      <text x="70" y="68" text-anchor="middle" font-family="Quicksand, sans-serif" font-weight="700" font-size="13" fill="var(--grey-ring)">29</text>
      <rect x="20" y="13" width="32" height="10" rx="5" fill="var(--grey-ring)"/>
      <text class="ring-label" x="36" y="20" text-anchor="middle">Renting</text>
      <rect x="92" y="38" width="44" height="10" rx="5" fill="var(--green)"/>
      <text class="ring-label" x="114" y="45" text-anchor="middle">Fully Owned</text>
      <rect x="32" y="84" width="40" height="10" rx="5" fill="var(--navy)"/>
      <text class="ring-label" x="52" y="91" text-anchor="middle">Purchasing</text>
    </svg>
  </div>

  <div class="footer-band"></div>
  <div class="brand">Slate Ridge</div>
  <div class="web">www.slateridge.com</div>
</section>

</body>
</html>
```